Website for Reiki and Wellness Courses

I teach online courses in Reiki and wellness/self-development and am needing a new website.

The focus of the website will be to provide descriptions of the courses as well as include a blog and pages where students in my courses will visit for additional information.

Note: courses are NOT hosted on this site.
The focus of this website will be to encourage viewers to enroll in courses as well as opt in to the email list.

I will upload copy soon. My old website is: http://calmstreamlessons.example. Please do not use existing logo.

Target Market(s)

Alternative health, wellness, spirituality, personal development. Males and females of all ages seeking to improve their health and life.

Industry/Entity Type

Health And Wellness

Logo Text

No text (please do not use existing logo)

Coding

Coded - Design and coding required

Number of Pages Required

5+ page

Requirements
Must have
• 1. Home page
• 2. About page
• 3. Courses page that outlines courses (there are currently 6 courses with 1 coming soon)
• 4. Individual course page (maybe a template that I can adjust color and pictures for with each course)
• 5. Blog
• 6. Student Area that outlines all Student Areas
• 7. Individual Student Area page (maybe a template that I can adjust color and pictures for with each course)
• 8. Shop page (note: items will not currently be purchased through website - it will be a link to brightmart for a book).
• 9. Student thank-you page (maybe a template that I can adjust color and pictures for with each course) this is the page students are directed to at end of course with vouchers for other courses.
• Opt-in for the home page, course pages, blog and thank-you pages
Nice to have
• I would like the design to be calm, clean and soothing. Ideally visitors feel relaxed when viewing the site and are encouraged to explore the courses, subscribe to the email list and purchase a product.
• ~ Testimonials page
• ~ Contact page
• I tend to gravitate towards blues, greys and purples as well as monochromatic color schemes.
Should not have
• Contact form on home page
• phone number on home page
• location/physical address
• dates for blog posts

```html
<!DOCTYPE html>
<html lang="en">
<head>
<meta charset="utf-8">
<title>Calm Stream Lessons</title>
<link rel="stylesheet" href="https://fonts.googleapis.com/css2?family=Open+Sans:wght@400;600&display=swap">
<style>
:root{
  --ink:#4a4c5e;
  --slate:#6e7190;
  --slate-dark:#5f6280;
  --muted:#7a7a80;
  --line:#c9c9cf;
  --paper:#ffffff;
  --mist:#f2f2f3;
  --footer:#3a3a3c;
  --footer-text:#b4b4b8;
  --social-1:#3b5b9a;
  --social-2:#3a9fdc;
  --social-3:#2f73b0;
}
*{box-sizing:border-box;margin:0;padding:0}
html,body{width:782px;height:1200px;overflow:hidden;background:var(--paper)}
body{position:relative;font-family:"Open Sans",Arial,sans-serif;color:var(--ink)}
.abs{position:absolute}

/* header */
.site-header{left:0;top:0;width:782px;height:56px;background:var(--paper);border-bottom:1px solid #e4e4e8}
.brand{left:86px;top:18px;display:flex;align-items:center;gap:7px;font-size:13px;font-weight:600;color:var(--slate)}
.brand-dot{width:16px;height:16px;border-radius:50%;background:var(--slate)}
.main-nav{right:88px;top:24px;display:flex;gap:20px;font-size:8px;color:var(--muted)}

/* hero */
.hero{left:0;top:56px;width:782px;height:234px;
  background:radial-gradient(circle at 20% 40%,#f6c39a 0%,rgba(246,195,154,0) 45%),
             radial-gradient(circle at 75% 30%,#f7d8e6 0%,rgba(247,216,230,0) 50%),
             linear-gradient(100deg,#f1b58f 0%,#f3c9cf 45%,#efc4dd 75%,#f5dbe8 100%)}
.hero-title{right:88px;top:80px;font-size:22px;font-weight:600;color:#1d1d22;letter-spacing:.2px}
.hero-sub{right:88px;top:111px;font-size:8px;color:#2b2b30}
.hero-btn{left:636px;top:183px;width:58px;height:23px;background:var(--paper);font-size:7px;color:var(--muted);display:flex;align-items:center;justify-content:center}
.dots{display:flex;gap:8px}
.dot{width:6px;height:6px;border-radius:50%;background:#7a7d90}
.hero .dots{position:absolute;left:364px;top:212px}
.dot.hollow{background:transparent;border:1px solid #7a7d90}

/* features */
.feature{top:310px;width:210px;text-align:center}
.feature svg{display:block;margin:0 auto;stroke:var(--slate);fill:none;stroke-width:1.2}
.feature h2{font-size:14px;font-weight:400;color:var(--slate);line-height:15px;margin-top:12px;height:30px;display:flex;align-items:center;justify-content:center}
.feature p{font-size:6.5px;color:var(--muted);margin-top:6px}
.btn-outline{display:inline-block;margin-top:11px;width:53px;height:21px;border:1px solid var(--line);font-size:6.5px;color:var(--muted);line-height:19px}

/* blog */
.blog{left:0;top:482px;width:782px;height:240px;background:var(--mist)}
.section-title{font-size:16px;font-weight:400;color:var(--slate)}
.blog-title{left:86px;top:23px}
.arrows{left:660px;top:27px;display:flex;gap:5px}
.arrow{width:15px;height:14px;border:1px solid #a9a9b0;background:var(--paper);display:flex;align-items:center;justify-content:center}
.post{top:55px;width:193px}
.post-media{width:193px;height:114px}
.post h3{font-size:8px;font-weight:400;color:#2e2e34;line-height:11px;margin-top:10px}
.post a{display:block;font-size:5.8px;color:var(--muted);margin-top:9px;text-decoration:none}

/* testimonials */
.testimonials-title{left:0;top:756px;width:782px;text-align:center}
.ghost{top:780px;width:110px;height:130px;background:linear-gradient(90deg,rgba(236,236,238,0),#ececee)}
.quote-card{left:179px;top:780px;width:422px;height:130px;background:var(--slate);border-radius:3px;color:#fff;text-align:center;padding:15px 20px 0}
.quote-card h4{font-size:9.5px;font-weight:400}
.quote-card p{font-size:6.1px;line-height:12.4px;margin-top:3px}
.quote-card .author{font-size:8.5px;margin-top:4px}
.quote-tail{left:380px;top:909px;width:0;height:0;border-left:10px solid transparent;border-right:10px solid transparent;border-top:10px solid var(--slate)}
.testimonial-dots{left:363px;top:932px}
.testimonial-dots .dot{width:7px;height:7px;background:#c8c8cc}
.testimonial-dots .dot.on{background:#222}

/* opt-in */
.optin{left:0;top:982px;width:782px;height:130px;background:var(--mist);text-align:center}
.optin .section-title{margin-top:22px}
.optin p{font-size:7px;line-height:11px;color:var(--muted);width:600px;margin:6px auto 0}
.field{top:79px;width:143px;height:26px;background:var(--paper);border:1px solid var(--line);font-size:7px;color:var(--muted);text-align:left;padding-left:10px;line-height:24px}
.submit{left:575px;top:79px;width:84px;height:26px;background:var(--slate);color:#fff;font-size:8px;line-height:26px;border:1px solid var(--slate-dark)}

/* footer */
.site-footer{left:0;top:1112px;width:782px;height:88px;background:var(--footer)}
.footer-nav{left:86px;top:30px;font-size:6.5px;color:var(--footer-text);display:flex;gap:6px}
.copyright{left:86px;top:49px;font-size:6.5px;color:var(--footer-text)}
.footer-mark{left:379px;top:31px;width:22px;height:22px;border-radius:50%;background:#55555a}
.social{left:635px;top:36px;display:flex;gap:5px}
.social span{width:17px;height:17px;border-radius:50%}
</style>
</head>
<body>

<header class="site-header abs">
  <div class="brand abs"><span class="brand-dot"></span>Calm Stream Lessons</div>
  <nav class="main-nav abs"><span>Home</span><span>About</span><span>Courses</span><span>Blog</span><span>Students Area</span><span>Contact</span></nav>
</header>

<section class="hero abs" role="img" aria-label="Open palm beneath glowing Reiki lettering on a warm pink and peach bokeh background">
  <h1 class="hero-title abs">Time for Change in Your Life</h1>
  <p class="hero-sub abs">What would it be like to live the life you were meant to live?</p>
  <div class="hero-btn abs">Learn More</div>
  <div class="dots"><span class="dot hollow"></span><span class="dot"></span><span class="dot"></span><span class="dot"></span></div>
</section>

<div class="feature abs" style="left:75px">
  <svg width="52" height="40" viewBox="0 0 52 40"><rect x="4" y="6" width="18" height="30" rx="8"/><rect x="30" y="6" width="18" height="30" rx="8"/></svg>
  <h2>How Reiki Works</h2>
  <p>Reiki has been used for centuries to help individuals...</p>
  <span class="btn-outline">Read more</span>
</div>
<div class="feature abs" style="left:285px">
  <svg width="46" height="30" viewBox="0 0 46 30"><rect x="1" y="1" width="44" height="28"/><rect x="5" y="6" width="12" height="18"/><line x1="21" y1="9" x2="40" y2="9"/><line x1="21" y1="15" x2="40" y2="15"/><line x1="21" y1="21" x2="40" y2="21"/></svg>
  <h2>Traditional Usui Reiki<br>Master Certification</h2>
  <p>Learn how to use Reiki to help yourself and others.</p>
  <span class="btn-outline">Read more</span>
</div>
<div class="feature abs" style="left:496px">
  <svg width="38" height="36" viewBox="0 0 38 36"><path d="M2 1h20l6 6v28H2z"/><path d="M10 6h20l6 6v23"/><line x1="6" y1="12" x2="22" y2="12"/><line x1="6" y1="17" x2="22" y2="17"/><line x1="6" y1="22" x2="22" y2="22"/><line x1="6" y1="27" x2="22" y2="27"/></svg>
  <h2>Resources</h2>
  <p>Information and tools to help you create a life you love.</p>
  <span class="btn-outline">Read more</span>
</div>

<section class="blog abs">
  <h2 class="section-title blog-title abs">Blog</h2>
  <div class="arrows abs">
    <span class="arrow"><svg width="6" height="8" viewBox="0 0 6 8"><path d="M5 1L2 4l3 3" fill="none" stroke="#777" stroke-width="1"/></svg></span>
    <span class="arrow"><svg width="6" height="8" viewBox="0 0 6 8"><path d="M1 1l3 3-3 3" fill="none" stroke="#777" stroke-width="1"/></svg></span>
  </div>
  <article class="post abs" style="left:86px">
    <div class="post-media" role="img" aria-label="Reiki session with a client resting on a treatment table" style="background:linear-gradient(135deg,#e8d2bd,#b98e72 55%,#7a4a6a)"></div>
    <h3>Aenean sed quam non sapien faucibus consequat vitae sit amet orci</h3>
    <a>READ MORE</a>
  </article>
  <article class="post abs" style="left:294px">
    <div class="post-media" role="img" aria-label="Two hands channelling energy on a pale background" style="background:linear-gradient(135deg,#fbfbfb,#ece6e2 60%,#f6f4f2)"></div>
    <h3>Aenean sed quam non sapien faucibus consequat vitae sit amet orci</h3>
    <a>READ MORE</a>
  </article>
  <article class="post abs" style="left:502px">
    <div class="post-media" role="img" aria-label="Hands giving Reiki to a small white dog" style="background:linear-gradient(135deg,#8fb0d4,#e8e4df 50%,#7d9cc4)"></div>
    <h3>Aenean sed quam non sapien faucibus consequat vitae sit amet orci</h3>
    <a>READ MORE</a>
  </article>
</section>

<h2 class="section-title testimonials-title abs">Testimonials</h2>
<div class="ghost abs" style="left:56px"></div>
<div class="ghost abs" style="left:614px;background:linear-gradient(90deg,#ececee,rgba(236,236,238,0))"></div>
<div class="quote-card abs">
  <h4>&#8220; A very thorough and authentic training</h4>
  <p>I really loved this course. The lectures were enjoyable to listen to. It was a great feature to offer them as additional downloads. The extra material like the guided meditations were all high quality. As someone very familiar with Japanese culture I really appreciated the accuracy and authenticity of the material as well as the thoroughness of the training, covering many techniques and methods. Arranging the attunements was very straightforward and I would highly recommend this course to anyone interested in Reiki. &#8221;</p>
  <div class="author">~ Marisa Thornfield</div>
</div>
<div class="quote-tail abs"></div>
<div class="dots testimonial-dots abs"><span class="dot on"></span><span class="dot"></span><span class="dot"></span><span class="dot"></span></div>

<section class="optin abs">
  <h2 class="section-title">Stay Inspired</h2>
  <p>Receive information and articles each month to keep you feeling inspired. As a thank-you, you will also receive access to soothing music you can download for use in your Reiki sessions and meditation.</p>
  <div class="field abs" style="left:123px">First Name</div>
  <div class="field abs" style="left:274px">Last Name</div>
  <div class="field abs" style="left:425px">Email Address</div>
  <div class="submit abs">Yes-Count Me In</div>
</section>

<footer class="site-footer abs">
  <nav class="footer-nav abs"><span>Home</span><span>|</span><span>About</span><span>|</span><span>Courses</span><span>|</span><span>Blog</span><span>|</span><span>Students Area</span><span>|</span><span>Contact</span></nav>
  <p class="copyright abs">Copyright &copy; 2016 &nbsp;Calm Stream Lessons. &nbsp;All rights reserved.</p>
  <div class="footer-mark abs"></div>
  <div class="social abs"><span style="background:var(--social-1)"></span><span style="background:var(--social-2)"></span><span style="background:var(--social-3)"></span></div>
</footer>

</body>
</html>
```